#ZELTO

#Zelto is the business name. I need a marketing brochure to show potential clients. The concept is providing the restaurant trade and function centres with volume wine in large wine casks and then on-sell by the glass or in varying carafe sizes. The advantages will be outlined in the file provided I want to introduce the concept and demonstrate the advantages visusally

Restaurant

```html
<!DOCTYPE html>
<html lang="en">
<head>
<meta charset="utf-8">
<title>Zelto — volume wine for the restaurant trade</title>
<link rel="stylesheet" href="https://fonts.googleapis.com/css2?family=Tenor+Sans&display=swap">
<style>
  :root {
    --bg-ink: #140607;
    --text-light: #f4efea;
    --wood-light: #d9a66a;
    --wood-mid: #a8683a;
    --wood-dark: #3b1a0c;
    --wine-amber: #c45a1a;
  }
  * { margin: 0; padding: 0; box-sizing: border-box; }
  html, body {
    width: 1200px;
    height: 2437px;
    overflow: hidden;
    background: var(--bg-ink);
  }
  .brochure {
    position: relative;
    width: 1200px;
    height: 2437px;
    background: var(--bg-ink);
    color: var(--text-light);
    font-family: "Tenor Sans", "Optima", sans-serif;
  }
  .brand-name {
    position: absolute;
    left: 74px;
    top: 200px;
    font-family: "Tenor Sans", "Optima", sans-serif;
    font-weight: 400;
    font-size: 110px;
    line-height: 1;
    letter-spacing: 6px;
    color: var(--text-light);
  }
  .intro {
    position: absolute;
    left: 77px;
    top: 432px;
    width: 1090px;
    font-size: 31px;
    line-height: 37px;
  }
  .advantages {
    position: absolute;
    left: 77px;
    top: 585px;
    width: 1040px;
    font-size: 31px;
    line-height: 59px;
  }
  .advantages-heading {
    font-size: 31px;
    line-height: 59px;
    font-weight: 400;
    -webkit-text-stroke: 0.8px var(--text-light);
  }
  .advantages-list { list-style: none; }
  .carafe-note {
    position: absolute;
    left: 83px;
    top: 1306px;
    font-size: 31px;
    line-height: 37px;
  }
  .hero-photo {
    position: absolute;
    left: 0;
    top: 1533px;
    width: 1200px;
    height: 904px;
    background:
      radial-gradient(ellipse 300px 330px at 860px 330px, var(--wine-amber) 0%, rgba(196,90,26,0.5) 45%, rgba(0,0,0,0) 75%),
      linear-gradient(160deg, var(--wood-dark) 0%, var(--wood-mid) 30%, var(--wood-light) 50%, var(--wood-mid) 70%, var(--wood-dark) 100%);
  }
</style>
</head>
<body>
  <main class="brochure">
    <h1 class="brand-name">Zelto</h1>

    <p class="intro">Providing the restaurant trade with a more effective, economical and sustainable alternative to wine retail.</p>

    <section class="advantages">
      <h2 class="advantages-heading">The advantages of using #ZELTO concept:</h2>
      <ul class="advantages-list">
        <li>- The cask wine uses less storage space</li>
        <li>- Eco friendly, no glass.</li>
        <li>- Larger quantity better margins</li>
        <li>- Longer shelf life</li>
        <li>- No wastage</li>
        <li>- More Hygienic</li>
        <li>- Wine sourced from reputable growers in well-known regions of New Zealand, Barossa Valley and Tasmania. Cask sizes will start from 10ltrs and up to 22ltrs Aesthetic Urns or Wine barrels to hide cask that will come in either 15ltr, 25ltr and will fit all cask sizes.</li>
      </ul>
    </section>

    <p class="carafe-note">Carafe glassware available too: in 250ml, 500ml and 1000ml sizes.</p>

    <div class="hero-photo" role="img" aria-label="Photo of a glass of red wine on a sunlit wooden table, casting a warm shadow"></div>
  </main>
</body>
</html>
```